Australian Sports Podiatry Business needs a Vantor Summerfest marketing flyer

The Stride Hub is looking for a double sided DLflyer to send out to homes which is targeted at people interested in being fit and healthy. To include:

the Vantor Summerfest logo and colours
sporty background

Are you Ready For Vantor?
Whatever Your Goals, We'll Keep You On Track
National and International Sports Experience
Lorvane Ablegames (and logo if possible)
Kestrow Unity Crown Games (and logo if poss)
Dunmere Tri-Sport Global Finals (+logo)
Dunmere Galloway Shield Tennis (+logo)

The Stride Hub name, logo, phone number 9271 6028, website www.thestridehub.example, email info@thestridehub.example

Dr Marek Ondravelli's Background:
Marek's has 20 years experience in the field of Sports Medicine and lower limb biomechanics, and he has had extensive experience with treatment of elite athletes from the Calbrook Institute of Athletics, the Fenwell Athletes Lodge, the Calbrook Stormhawks, Tolvane Harriers and the Tolvane Nightjars. He was also selected for the BRELT Medical Team to provide Podiatry Services at the Lorvane 2000 Ablegames, the 2000 GMV Global Tri-Sport Finals, the Kestrow 2006 Unity Crown Games and the Dunmere 2013 Galloway Shield. Marek now treats many athletes from all disciplines in Perth and surrounding areas.

In 1999 Marek became the Director and Senior Podiatrist for The Stride Hub in Perth, Western Australia. Since then he has also been a Director of Athletic Care Federation (ACF), WA Director for the Southern College of Lower-Limb Exercise Care (SCLEC), and an External Advisor to the Halvorne Coastal University’s Podiatric Medicine Unit. He is currently road testing minimalist running shoes for optimised performance and injury prevention.

Marek has always been involved with high level sports, having held a 4x400m Australian Record and also played 1st Division Hockey. He is now training for the Veterans Track Global Finals in October, and volunteers at Quenby Comets Junior Track. He also enjoys keeping fit by running after his 3 kids Brisa, Matilde, and Oskar.

Target Market(s)

People interested in being fit and healthy

Industry/Entity Type

Medical

Requirements
Must have
• To include:
• the Vantor Summerfest logo and colours
• sporty background
• Are you Ready For Vantor?
• Whatever Your Goals, We'll Keep You On Track
• National and International Sports Experience
• Lorvane Ablegames (and logo if possible)
• Kestrow Unity Crown Games (and logo if poss)
• Dunmere Tri-Sport Global Finals (+logo)
• Dunmere Galloway Shield Tennis (+logo)
• The Stride Hub name, logo, phone number 9271 6028, website www.thestridehub.example, email info@thestridehub.example
• Dr Marek Ondravelli's Background:
• Marek's has 20 years experience in the field of Sports Medicine and lower limb biomechanics, and he has had extensive experience with treatment of elite athletes from the Calbrook Institute of Athletics, the Fenwell Athletes Lodge, the Calbrook Stormhawks, Tolvane Harriers and the Tolvane Nightjars. He was also selected for the BRELT Medical Team to provide Podiatry Services at the Lorvane 2000 Ablegames, the 2000 GMV Global Tri-Sport Finals, the Kestrow 2006 Unity Crown Games and the Dunmere 2013 Galloway Shield. Marek now treats many athletes from all disciplines in Perth and surrounding areas.
• In 1999 Marek became the Director and Senior Podiatrist for The Stride Hub in Perth, Western Australia. Since then he has also been a Director of Athletic Care Federation (ACF), WA Director for the Southern College of Lower-Limb Exercise Care (SCLEC), and an External Advisor to the Halvorne Coastal University’s Podiatric Medicine Unit. He is currently road testing minimalist running shoes for optimised performance and injury prevention.
Nice to have
• Marek has always been involved with high level sports, having held a 4x400m Australian Record and also played 1st Division Hockey. He is now training for the Veterans Track Global Finals in October, and volunteers at Quenby Comets Junior Track. He also enjoys keeping fit by running after his 3 kids Brisa, Matilde, and Oskar.

```html
<!DOCTYPE html>
<html lang="en">
<head>
<meta charset="utf-8">
<title>The Stride Hub – DL Flyer</title>
<link rel="stylesheet" href="https://fonts.googleapis.com/css2?family=Oswald:wght@500;700&family=PT+Sans:wght@400;700&display=swap">
<style>
  :root {
    --stage: #5c3816;
    --blue-deep: #1a3f8f;
    --blue-mid: #2557b0;
    --blue-text: #1f55b0;
    --navy-name: #2a3a9a;
    --yellow: #f6e71c;
    --lime: #9cc83a;
    --red-dot: #d8232a;
    --white: #ffffff;
    --paper: #f2f2f0;
    --body-text: #2b2b2b;
  }
  * { box-sizing: border-box; margin: 0; padding: 0; }
  html, body { width: 1200px; height: 1200px; overflow: hidden; background: var(--stage); }
  body { position: relative; font-family: "PT Sans", sans-serif; }

  .side { position: absolute; left: 98px; width: 1018px; height: 452px; overflow: hidden; box-shadow: 0 6px 14px rgba(0,0,0,.35); }
  .side--front { top: 109px; background: linear-gradient(90deg, var(--blue-deep) 0%, var(--blue-mid) 45%, #2a5fb3 60%); }
  .side--back { top: 607px; background: var(--paper); }

  .abs { position: absolute; }

  /* front */
  .hero-photo { position: absolute; right: 0; top: 0; width: 460px; height: 452px;
    background: linear-gradient(90deg, rgba(42,95,179,1) 0%, rgba(120,110,95,.85) 25%, #b58a6c 45%, #8fb83a 62%, #7d8388 78%, #3b3b3d 100%); }
  .hero-photo::after { content: ""; position: absolute; inset: 0;
    background: linear-gradient(180deg, rgba(0,0,0,0) 55%, rgba(40,38,36,.7) 100%); }

  .headline { left: 34px; top: 28px; font-family: "Oswald", sans-serif; font-weight: 700; font-size: 52px; line-height: 1; color: var(--white); white-space: nowrap; text-shadow: 0 2px 3px rgba(0,0,0,.35); }
  .experience { left: 34px; top: 112px; font-size: 27px; line-height: 32px; color: var(--white); }
  .goals { left: 34px; top: 204px; font-size: 27px; line-height: 32px; color: var(--yellow); font-weight: 700; }

  .events { left: 414px; top: 226px; list-style: none; color: var(--white); font-size: 15px; line-height: 25px; }
  .events li { padding-left: 22px; position: relative; white-space: nowrap; }
  .events li::before { content: ""; position: absolute; left: 0; top: 7px; width: 12px; height: 12px; border-radius: 50%; background: var(--red-dot); }

  .call-splash { left: 515px; top: 130px; width: 250px; height: 60px; background: var(--lime); transform: rotate(-13deg); border-radius: 6px; display: flex; flex-direction: column; align-items: center; justify-content: center; color: var(--white); }
  .call-splash .call-label { font-family: "Oswald", sans-serif; font-weight: 500; font-size: 14px; line-height: 1.1; }
  .call-splash .call-number { font-family: "Oswald", sans-serif; font-weight: 700; font-size: 28px; line-height: 1.05; }

  .white-box { position: absolute; background: var(--white); border-radius: 6px; display: flex; align-items: center; justify-content: center; }
  .event-box { left: 33px; top: 305px; width: 228px; height: 102px; }
  .event-name { font-family: "PT Sans", sans-serif; font-weight: 700; font-size: 22px; color: var(--blue-deep); text-align: center; line-height: 1.1; }
  .brand-box { left: 264px; top: 289px; width: 119px; height: 130px; flex-direction: column; gap: 8px; box-shadow: 0 2px 5px rgba(0,0,0,.3); }
  .brand-dot { width: 58px; height: 58px; border-radius: 50%; background: var(--blue-mid); }
  .brand-name { font-size: 15px; color: var(--blue-mid); font-weight: 400; white-space: nowrap; }
  .partner-box { left: 385px; top: 323px; width: 265px; height: 64px; justify-content: space-around; padding: 0 10px; }
  .badge { width: 46px; height: 40px; border-radius: 6px; background: #d7e0ee; }

  .front-email { left: 40px; top: 414px; font-size: 13px; color: var(--white); white-space: nowrap; }
  .front-web { left: 412px; top: 396px; font-family: "Oswald", sans-serif; font-weight: 700; font-size: 25px; letter-spacing: 1.5px; color: var(--yellow); white-space: nowrap; }

  /* back */
  .bio-name { left: 40px; top: 18px; font-family: "Oswald", sans-serif; font-weight: 700; font-size: 27px; color: var(--navy-name); }
  .bio { left: 40px; width: 552px; font-size: 12.5px; line-height: 19px; color: var(--body-text); text-align: justify; }
  .bio--one { top: 62px; }
  .bio--two { top: 202px; }
  .divider { left: 647px; top: 38px; width: 1px; height: 252px; background: #c9c9c9; }
  .bio-side { left: 700px; top: 28px; width: 278px; font-size: 17.2px; line-height: 26.7px; color: var(--blue-text); text-align: justify; font-weight: 700; }

  .contact-band { position: absolute; left: 0; top: 306px; width: 1018px; height: 146px; background: linear-gradient(90deg, var(--blue-deep), var(--blue-mid) 60%, var(--blue-deep)); }
  .clinic-photo { position: absolute; top: 13px; height: 108px; border-radius: 6px; border: 2px solid var(--white); }
  .clinic-photo--1 { left: 38px; width: 108px; background: linear-gradient(135deg, #e7e6e2, #8f8f94); }
  .clinic-photo--2 { left: 153px; width: 128px; background: linear-gradient(135deg, #6c5b59, #c8b9a8 50%, #3c2f2c); }
  .clinic-photo--4 { left: 393px; width: 115px; background: linear-gradient(135deg, #a08a7c, #5f6f8a 60%, #2f3540); }
  .clinic-photo--5 { left: 513px; width: 115px; background: linear-gradient(135deg, #e0a070, #f3e1cf 50%, #c8693a); }
  .band-brand { left: 288px; top: 13px; width: 97px; height: 108px; gap: 6px; flex-direction: column; }
  .band-brand .brand-dot { width: 50px; height: 50px; }
  .band-brand .brand-name { font-size: 13px; }

  .band-call { left: 645px; top: 14px; color: var(--white); font-family: "Oswald", sans-serif; font-weight: 500; font-size: 19px; white-space: nowrap; }
  .band-call strong { font-weight: 700; font-size: 30px; }
  .band-web { left: 645px; top: 60px; font-family: "Oswald", sans-serif; font-weight: 700; font-size: 24px; letter-spacing: 1.2px; color: var(--yellow); white-space: nowrap; }
  .band-email { left: 645px; top: 98px; font-size: 19px; color: var(--white); letter-spacing: .3px; white-space: nowrap; }
</style>
</head>
<body>

<section class="side side--front">
  <div class="hero-photo" role="img" aria-label="Close-up photo of a runner's foot in a lime running shoe on a track"></div>

  <h1 class="abs headline">ARE YOU READY FOR VANTOR?</h1>
  <p class="abs experience">NATIONAL AND INTERNATIONAL<br>SPORTS EXPERIENCE</p>
  <p class="abs goals">WHATEVER YOUR GOALS,<br>WE'LL KEEP YOU ON TRACK</p>

  <div class="abs call-splash">
    <span class="call-label">Call to The Stride Hub:</span>
    <span class="call-number">9271 6028</span>
  </div>

  <ul class="abs events">
    <li>Lorvane Ablegames,</li>
    <li>Kestrow Unity Crown Games,</li>
    <li>Dunmere Tri-Sport Global Finals,</li>
    <li>Dunmere Galloway Shield Tennis</li>
  </ul>

  <div class="white-box event-box"><span class="event-name">Vantor Summerfest</span></div>
  <div class="white-box brand-box">
    <span class="brand-dot"></span>
    <span class="brand-name">The Stride Hub</span>
  </div>
  <div class="white-box partner-box">
    <span class="badge"></span><span class="badge"></span><span class="badge"></span><span class="badge"></span>
  </div>

  <p class="abs front-email">email info@thestridehub.example</p>
  <p class="abs front-web">www.thestridehub.example</p>
</section>

<section class="side side--back">
  <h2 class="abs bio-name">Dr Marek Ondravelli</h2>
  <p class="abs bio bio--one">Marek's has 20 years experience in the field of Sports Medicine and lower limb biomechanics, and he has had extensive experience with treatment of elite athletes from the Calbrook Institute of Athletics, the Fenwell Athletes Lodge, the Calbrook Stormhawks, Tolvane Harriers and the Tolvane Nightjars. He was also selected for the BRELT Medical Team to provide Podiatry Services at the Lorvane 2000 Ablegames, the 2000 GMV Global Tri-Sport Finals, the Kestrow 2006 Unity Crown Games and the Dunmere 2013 Galloway Shield. Marek now treats many athletes from all disciplines in Perth and surrounding areas.</p>
  <p class="abs bio bio--two">In 1999 Marek became the Director and Senior Podiatrist for The Stride Hub in Perth, Western Australia. Since then he has also been a Director of Athletic Care Federation (ACF), WA Director for the Southern College of Lower-Limb Exercise Care (SCLEC), and an External Advisor to the Halvorne Coastal University's Podiatric Medicine Unit. He is currently road testing minimalist running shoes for optimised performance and injury prevention.</p>
  <div class="abs divider"></div>
  <p class="abs bio-side">Marek has always been involved with high level sports, having held a 4x400m Australian Record and also played 1st Division Hockey. He is now training for the Veterans Track Global Finals in October, and volunteers at Quenby Comets Junior Track. He also enjoys keeping fit by running after his 3 kids Brisa, Matilde, and Oskar.</p>

  <div class="contact-band">
    <div class="clinic-photo clinic-photo--1" role="img" aria-label="Photo of a podiatrist examining a patient's foot"></div>
    <div class="clinic-photo clinic-photo--2" role="img" aria-label="Photo of a podiatrist reviewing x-rays with a patient"></div>
    <div class="white-box band-brand">
      <span class="brand-dot"></span>
      <span class="brand-name">The Stride Hub</span>
    </div>
    <div class="clinic-photo clinic-photo--4" role="img" aria-label="Photo of a gait analysis on a treadmill"></div>
    <div class="clinic-photo clinic-photo--5" role="img" aria-label="Photo of hands taking a plaster cast of a foot"></div>

    <p class="abs band-call">Call to The Stride Hub: <strong>9271 6028</strong></p>
    <p class="abs band-web">www.thestridehub.example</p>
    <p class="abs band-email">email info@thestridehub.example</p>
  </div>
</section>

</body>
</html>
```